Banner Ad Needed For Real Estate Lending Firm

We are taking out a banner ad on one of the most highly trafficked real estate websites in New York. The ad will be 970x250. Display format will be JPEG or animated GIF, but original art files will be required as well from the winning designer.

Granite Path Lending (or GPL) is one of the largest "hard money lenders" for real estate investors on the East Coast of the US. We lend for the following real estate investments: 1) Fix And Flip 2) New Construction 3) Cash Out Refinance. We close in 2-10 days. More information can be found on our website here: http://www.gpl7.example/

Our goal is to help small business owners, real estate investors, and commercial contractors quickly and efficiently finance their business activities. Our local hard money loan programs are tailored to your unique project needs. We fund fix and flip, new construction, and cash out refinance projects for non-owner occupied properties.

Target Market(s)

Real Estate Agents, Real Estate Investors, Mortgage Brokers, Other Real Estate Professionals

Industry/Entity Type

Real Estate

Font styles to use
Sans Serif

Requirements
Must have
• Must incorporate the fact that we close deals very fast (2 - 10 days), finance the following these 2 main types of investments (Fix and Flip, New Construction), and mention that Brokers can make up to 2.5 Points.
• See attached style guide for basic colors and fonts.
Nice to have
• Animated GIF might be a great feature!

```html
<!DOCTYPE html>
<html lang="en">
<head>
<meta charset="utf-8">
<title>Granite Path Lending – Banner</title>
<link rel="stylesheet" href="https://fonts.googleapis.com/css2?family=Roboto:wght@400;500&display=swap">
<style>
  :root {
    --teal: #4f8b7c;
    --teal-dark: #3e7a6c;
    --white: #ffffff;
    --photo-dark: #6f7a78;
    --photo-mid: #b8bfbd;
  }
  * { margin: 0; padding: 0; box-sizing: border-box; }
  html, body { width: 1200px; height: 309px; overflow: hidden; background: var(--white); }
  .banner {
    position: relative;
    width: 1200px;
    height: 309px;
    overflow: hidden;
    background: var(--white);
    font-family: "Roboto", Arial, sans-serif;
  }
  .banner__photo {
    position: absolute;
    left: 0; top: 60px;
    width: 390px; height: 249px;
    background:
      linear-gradient(90deg, rgba(255,255,255,0) 30%, var(--white) 100%),
      linear-gradient(180deg, var(--white) 0%, #dfe3e2 20%, var(--photo-mid) 55%, var(--photo-dark) 100%);
  }
  .brand {
    position: absolute;
    left: 26px; top: 14px;
    display: flex; align-items: center; gap: 16px;
  }
  .brand__dot {
    width: 46px; height: 46px;
    border-radius: 50%;
    background: var(--teal-dark);
  }
  .brand__name {
    font-size: 14px;
    font-weight: 500;
    line-height: 1.15;
    color: var(--teal-dark);
    text-transform: uppercase;
  }
  .headline {
    position: absolute;
    left: 394px; top: 52px;
    width: 300px;
    text-align: center;
    color: var(--teal);
    text-transform: uppercase;
  }
  .headline__lead { font-size: 42px; line-height: 1.08; font-weight: 400; }
  .headline__fast { font-size: 98px; line-height: 1; font-weight: 500; margin-top: 6px; }
  .headline__days { font-size: 32px; line-height: 1.1; font-weight: 500; margin-top: 6px; }
  .panel {
    position: absolute; left: 0; top: 0;
    width: 1200px; height: 309px;
  }
  .panel path { fill: var(--teal); }
  .programs {
    position: absolute;
    left: 734px; top: 64px;
    list-style: none;
    color: var(--white);
    font-size: 34px;
    font-weight: 400;
    text-transform: uppercase;
    line-height: 57px;
  }
  .broker-note {
    position: absolute;
    left: 736px; top: 248px;
    color: var(--white);
    font-size: 21px;
    font-weight: 500;
    text-transform: uppercase;
    letter-spacing: 0.5px;
  }
</style>
</head>
<body>
  <div class="banner">
    <div class="banner__photo" role="img" aria-label="Photo of a large white two-storey house with trees, fading into white"></div>

    <div class="brand">
      <span class="brand__dot"></span>
      <span class="brand__name">Granite<br>Path<br>Lending LLC</span>
    </div>

    <svg class="panel" width="1200" height="309" viewBox="0 0 1200 309" aria-hidden="true">
      <path d="M678 0 Q772 154.5 693 309 L1200 309 L1200 0 Z"/>
    </svg>

    <div class="headline">
      <p class="headline__lead">We close<br>deals very</p>
      <p class="headline__fast">Fast</p>
      <p class="headline__days">(2 - 10 days)</p>
    </div>

    <ol class="programs">
      <li>1 Fix and flip</li>
      <li>2 New construction</li>
      <li>3 Cash out refinance</li>
    </ol>

    <p class="broker-note">Brokers make up to 2.5 points</p>
  </div>
</body>
</html>
```